Advertising flyer for proofreading business.

Hello everyone,

I need an advertising flyer for a new proofreading company in Australia.

I would like your design in be in two sizes:
- A4 (to be posted on noticeboards),
- A6 (to be printed in larger quantity to give away)
(please see the size specification file attached).

The text file is attached (Ad Text) and it contains lots of information. Please feel free to include your choice of text from the text file, but please include Poster title, and highlight 'ESL' and students discounts.

I understand that it is impossible to include the same amount of information on A6 and A4, so please feel free to chose what fits on each of them, but please keep the design similar.

I have attached our company logo, but feel free to adjust it to the poster design (feel free to change the color as well). The original logo file contains circle around it, please feel free to remove it and include only the typeset as it can be seen here: http://www.lexmarka.com.au/.

Flyers will be printed, so please see the specification file for details.

I will do my best to respond to feedback as soon as possible.

I appreciate your participation, time and help,
Best wishes,
Bartosz

Target Market(s)

Students, authors

Industry/Entity Type

Business

Colors

Designer to choose colors to be used in the design.

Requirements
Must have
• It would be good if poster is easy to spot on busy noticeboards and attract attention.
• Please keep the poster in the positive/optimistic mood, and so that it focuses on students, maybe photos of graduates(?).
• Poster title,
• Please include the list of proof-read documents as they are described in the attached text file (Ad Text).
• Please highlight students discounts and ESL.
Nice to have
• I would like to leave the creative freedom to all designers so at this point I have not adjusted the Look and Feel sliders. Please feel free to offer your own take on this.
• It would be nice if most of the text could be fit to the poster.

```html
<!DOCTYPE html>
<html lang="en">
<head>
<meta charset="utf-8">
<title>Lexmarka – Professional English Language Proofreading</title>
<link href="https://fonts.googleapis.com/css2?family=Ubuntu:wght@400;500;700&family=Raleway:wght@400;500&display=swap" rel="stylesheet">
<style>
  :root {
    --teal: #13a68d;
    --teal-dark: #0b8a74;
    --sky: #8fd3f2;
    --panel-light: #d7e6f6;
    --panel-mid: #a9c9ec;
    --orange: #f7a51c;
    --ink: #3a3d46;
    --white: #ffffff;
    --page: #ffffff;
  }
  * { margin: 0; padding: 0; box-sizing: border-box; }
  html, body { width: 1200px; height: 847px; overflow: hidden; background: var(--page); }
  body { position: relative; font-family: "Ubuntu", sans-serif; color: var(--ink); }

  .flyer {
    position: absolute; left: 337px; top: 55px;
    width: 525px; height: 736px; overflow: hidden;
    background: var(--panel-light);
  }
  .flyer-art { position: absolute; inset: 0; width: 525px; height: 736px; }

  .brand {
    position: absolute; left: 24px; top: 20px; width: 78px; height: 78px;
    border-radius: 50%; background: var(--teal);
    display: flex; align-items: center; justify-content: center;
    color: var(--white); font-weight: 500; font-size: 15px;
  }

  .title {
    position: absolute; left: 168px; top: 28px;
    color: var(--white); font-weight: 700; font-size: 25px; line-height: 30px;
  }
  .esl-callout {
    position: absolute; left: 332px; top: 133px;
    color: var(--teal); font-weight: 500; font-size: 17px; line-height: 18px;
  }
  .intro {
    position: absolute; right: 37px; top: 246px; width: 300px;
    text-align: right; font-weight: 500; font-size: 11px; line-height: 13.5px;
  }
  .intro p + p { margin-top: 6px; }

  .icon-badge {
    position: absolute; border-radius: 50%; background: var(--teal);
    display: flex; align-items: center; justify-content: center; color: var(--white);
  }
  .section-heading {
    position: absolute; color: var(--teal); font-weight: 700; font-size: 14px;
  }

  .service-list {
    position: absolute; list-style: none;
    font-family: "Raleway", sans-serif; font-size: 8.5px; line-height: 15.5px;
  }
  .service-list li { padding-left: 11px; position: relative; }
  .service-list li::before {
    content: "✔"; position: absolute; left: 0; color: var(--teal); font-size: 8px;
  }

  .price-box {
    position: absolute; border-radius: 3px; color: var(--white);
    font-size: 8px; font-weight: 500; line-height: 10px;
    padding: 3px 6px; display: flex; align-items: center;
  }
  .price-box--teal { background: var(--teal); }
  .price-box--orange { background: var(--orange); }

  .testimonial-heading { left: 111px; top: 604px; font-size: 10px; }
  .testimonial-quote {
    position: absolute; left: 111px; top: 618px; width: 200px;
    font-size: 6.5px; line-height: 8.5px; font-style: italic;
  }
  .testimonial-name {
    position: absolute; left: 111px; top: 648px;
    font-size: 6.5px; line-height: 8.5px;
  }
  .testimonial-name .name { color: var(--teal); }

  .contact-badge {
    position: absolute; left: 370px; top: 582px; width: 106px; height: 106px;
    border-radius: 50%; background: var(--orange); color: var(--white);
    text-align: center; display: flex; flex-direction: column; justify-content: center;
    font-size: 9px; font-weight: 700; line-height: 11px;
  }
  .contact-badge .details { font-weight: 400; font-size: 7.5px; margin-top: 4px; line-height: 10px; }
</style>
</head>
<body>
<main class="flyer">
  <svg class="flyer-art" viewBox="0 0 525 736">
    <defs>
      <linearGradient id="photoTone" x1="0" y1="0" x2="1" y2="1">
        <stop offset="0" stop-color="#4f7a32"/>
        <stop offset="0.45" stop-color="#2e4429"/>
        <stop offset="1" stop-color="#8ab65a"/>
      </linearGradient>
      <linearGradient id="panelTone" x1="0" y1="0" x2="1" y2="1">
        <stop offset="0" stop-color="#dfeaf7"/>
        <stop offset="1" stop-color="#a3c4ea"/>
      </linearGradient>
      <linearGradient id="bannerTone" x1="0" y1="0" x2="1" y2="0">
        <stop offset="0" stop-color="#13a68d"/>
        <stop offset="0.7" stop-color="#3dbfb0"/>
        <stop offset="1" stop-color="#8fd3f2"/>
      </linearGradient>
    </defs>

    <rect class="photo-area" x="0" y="0" width="525" height="480" fill="url(#photoTone)"
          role="img" aria-label="Photo: two smiling students sitting on the grass working on a laptop"/>

    <path class="banner" d="M104 0 H525 V111 H150 Z" fill="url(#bannerTone)" opacity="0.95"/>

    <path class="panel-curve-band" d="M0 385 C140 280 320 205 525 180 L525 200 C330 226 160 300 0 420 Z" fill="var(--teal)"/>
    <path class="panel" d="M0 405 C150 295 330 222 525 196 L525 736 L0 736 Z" fill="url(#panelTone)"/>

    <path class="swoosh" d="M0 420 C18 520 40 620 72 736 L0 736 Z" fill="var(--teal)"/>
    <path class="bottom-band" d="M40 736 C100 705 300 690 525 652 L525 736 Z" fill="var(--teal)"/>
  </svg>

  <div class="brand">Lexmarka</div>

  <h1 class="title">Professional, English<br>Language Proofreading.</h1>

  <p class="esl-callout">Help with English<br>as a second<br>language (ESL).</p>

  <div class="intro">
    <p>Proofreading by a<br>native English speaker<br>with an English Honours<br>degree.</p>
    <p>Includes correct all English language<br>errors, spelling and grammar mistakes,<br>reference checking and editing for style, coherence<br>and clarity.</p>
  </div>

  <div class="icon-badge" style="left:166px; top:361px; width:32px; height:32px;">
    <svg width="14" height="16" viewBox="0 0 14 16"><rect x="1" y="1" width="12" height="14" rx="1" fill="#fff"/><path d="M3.5 5h7M3.5 8h7M3.5 11h5" stroke="#13a68d" stroke-width="1.2"/></svg>
  </div>
  <h2 class="section-heading" style="left:205px; top:367px;">We will proofread your</h2>

  <ul class="service-list" style="left:200px; top:388px;">
    <li>Essays &amp; Assignments</li>
    <li>Theses</li>
    <li>Resumes</li>
    <li>Business Correspondence</li>
    <li>Training Manuals</li>
  </ul>
  <ul class="service-list" style="left:320px; top:388px;">
    <li>Newsletters</li>
    <li>Advertising Copy</li>
    <li>Brochures, Catalogues &amp; Media Releases</li>
    <li>Websites</li>
    <li>Presentations &amp; Speeches</li>
    <li>Novels &amp; Short Stories</li>
  </ul>

  <div class="icon-badge" style="left:73px; top:474px; width:34px; height:34px; font-size:20px;">$</div>
  <h2 class="section-heading" style="left:111px; top:483px;">Price guide</h2>

  <div class="price-box price-box--teal" style="left:69px; top:506px; width:230px; height:17px;">Prices start at only $20 (short menus, flyers, letters).</div>
  <div class="price-box price-box--orange" style="left:69px; top:527px; width:230px; height:27px;">Great student discount rate: $25 per hour (roughly 1000 words - 4 pages - of well-written text).</div>
  <div class="price-box price-box--teal" style="left:69px; top:560px; width:230px; height:27px;">Fast, negotiable time-frames (same day service available by special arrangement).</div>
  <div class="price-box price-box--orange" style="left:311px; top:506px; width:181px; height:28px;">Discounts for not-for-profit organisations and students.</div>
  <div class="price-box price-box--teal" style="left:311px; top:538px; width:181px; height:27px;">Package deals on documents over 50,000 words.</div>

  <div class="icon-badge" style="left:73px; top:603px; width:32px; height:32px;">
    <svg width="18" height="12" viewBox="0 0 18 12"><circle cx="6" cy="4" r="2.6" fill="none" stroke="#fff" stroke-width="1.2"/><circle cx="12" cy="4" r="2.6" fill="none" stroke="#fff" stroke-width="1.2"/><path d="M1 11c0-3 2.5-4 5-4s5 1 5 4M7 11c0-3 2.5-4 5-4s5 1 5 4" fill="none" stroke="#fff" stroke-width="1.2"/></svg>
  </div>
  <h2 class="section-heading testimonial-heading">Testimonial:</h2>
  <p class="testimonial-quote">Clara understood our requirements quickly and has been fantastic at delivering quality work, on time and within agreed budget. It's a pleasure to work with her.</p>
  <p class="testimonial-name"><span class="name">Rosa Whitfield</span><br>Operations Manager<br>Northline</p>

  <div class="contact-badge">
    <span>Contact us<br>for an obligation free<br>quote:</span>
    <span class="details">0400 123 456 /<br>hello@lexmarka.com.au</span>
  </div>
</main>
</body>
</html>
```